Skill Up Salary Up

Full Page
7.5 w x 10 h / 8 w x 10.75 h + .25" bleed
Full-Page Career Course Ad
Project Overview
• Goal: Create a visually attractive, modern, and uncluttered full-page magazine advertisement to list available career courses.
• Tone: Creative, professional, and attention-grabbing to prevent the reader from turning the page. The final design must prioritize readability.

Content Requirements
1. Header/Headline: Must be the primary focus. And grab peoples attention
2. Course Listing: A clear, well-organized list of the career courses.
________________________________________
Design & Aesthetic Directives
1. Layout & Readability (Crucial)
• The final ad must not look crowded or busy.
• Prioritize white space to make the text "breathe" and ensure the course list is easy to scan and read.
• Use a modern, clean, and professional typeface (font choice is critical for the aesthetic).
2. Visual Style
• Aim for a creative, modern, and fresh look. Avoid outdated or generic stock imagery/layouts.
3. Imagery/Graphic Element (Artist's Choice)
You have creative freedom regarding the main graphic element.
• Option A (Photography): Use a photo of a white male American with a collared shirt. The imagery should convey success, focus, or professional development.
• Option B (Vector/Illustration): Use a modern vector graphic, illustration, or abstract design. This could be used to symbolize growth, connection, or a career path.
The choice of graphic element is yours, but it must support the overall modern and uncrowded aesthetic.

Requirements
Must have
• Partial listing .. is part of the Harbor Lantern Course

```html
<!DOCTYPE html>
<html lang="en">
<head>
<meta charset="utf-8">
<title>Skill Up Salary Up – Upcoming KVL Courses</title>
<link rel="stylesheet" href="https://fonts.googleapis.com/css2?family=Teko:wght@500;600&family=Poppins:ital,wght@0,300;0,400;0,600;1,600&display=swap">
<style>
  :root {
    --stage: #575757;
    --paper: #ffffff;
    --card: #efefef;
    --card-shadow: #d5dae3;
    --photo-bg: #e3e3e3;
    --navy: #23508a;
    --blue-mid: #1f6f93;
    --teal: #1fa88f;
    --teal-badge: #1ea98e;
    --navy-badge: #244a8a;
    --ink: #111111;
    --white: #ffffff;
    --mint: #dff7f0;
  }
  * { margin: 0; padding: 0; box-sizing: border-box; }
  html, body { width: 891px; height: 1200px; overflow: hidden; background: var(--stage); }
  body { position: relative; font-family: 'Poppins', sans-serif; color: var(--white); }

  .page { position: absolute; left: 92px; top: 81px; width: 692px; height: 1038px; background: var(--paper); overflow: hidden; }
  .page > * { position: absolute; }

  .course-field { left: 0; top: 299px; width: 692px; height: 626px;
    background: linear-gradient(180deg, var(--navy) 0%, var(--blue-mid) 45%, var(--teal) 100%); }
  .header-art { left: 0; top: 0; width: 692px; height: 333px; }
  .hero-photo { left: 442px; top: 3px; width: 243px; height: 330px;
    background: radial-gradient(ellipse at 50% 45%, #f7f7f7 0%, #e8e8e8 55%, #dcdcdc 100%); }

  .t { position: absolute; line-height: 1; transform: translateY(-50%); white-space: nowrap; }

  .headline { font-family: 'Teko', sans-serif; font-weight: 600; line-height: 0.8; left: 46px; white-space: nowrap;
    background: linear-gradient(180deg, var(--navy) 0%, var(--teal) 100%);
    -webkit-background-clip: text; background-clip: text; color: transparent; }
  .headline--skill { top: 36px; font-size: 96px; }
  .headline--salary { top: 112px; font-size: 86px;
    background: linear-gradient(180deg, #1f8f92 0%, var(--teal) 100%);
    -webkit-background-clip: text; background-clip: text; }
  .subhead { font-family: 'Teko', sans-serif; font-weight: 500; font-size: 44px; color: var(--ink); left: 46px; top: 182px; transform: none; }
  .tagline { font-weight: 600; font-size: 13px; color: var(--ink); left: 45px; }

  .section-tab { background: var(--white); height: 35px; border-radius: 0 8px 8px 0; overflow: hidden; }
  .section-tab--right { border-radius: 8px 0 0 8px; }
  .section-title { font-family: 'Teko', sans-serif; font-weight: 600; font-size: 26px; line-height: 1;
    position: absolute; top: 50%; white-space: nowrap;
    transform: translateY(-42%) scaleX(0.86); transform-origin: left center;
    background: linear-gradient(180deg, #1f7e9c, var(--navy)); -webkit-background-clip: text; background-clip: text; color: transparent; }
  .section-title--long { font-size: 24px; }

  .label { font-weight: 600; font-size: 14px; }
  .item { font-weight: 300; font-size: 13.5px; }
  .note { font-weight: 600; font-style: italic; font-size: 12.5px; }
  .mint { color: var(--mint); font-weight: 400; }

  .tick { position: absolute; width: 15px; height: 15px; transform: translateY(-50%); }

  .badge { width: 78px; height: 78px; border-radius: 50%; display: flex; align-items: center; justify-content: center;
    text-align: center; font-weight: 600; font-size: 12.5px; line-height: 1.2; box-shadow: 3px 4px 8px rgba(0,0,0,0.18); }
  .badge--teal { background: var(--teal-badge); }
  .badge--navy { background: var(--navy-badge); }
</style>
</head>
<body>
<svg width="0" height="0" style="position:absolute">
  <defs>
    <symbol id="tick" viewBox="0 0 16 16">
      <path d="M13 5.5A6 6 0 1 1 9.5 2.2" fill="none" stroke="#fff" stroke-width="1.6" stroke-linecap="round"/>
      <path d="M4.5 7.5 L7.5 10.5 L14.5 2" fill="none" stroke="#fff" stroke-width="2.2" stroke-linecap="round" stroke-linejoin="round"/>
    </symbol>
  </defs>
</svg>

<main class="page">
  <div class="course-field"></div>

  <svg class="header-art" viewBox="0 0 692 333" aria-hidden="true">
    <path d="M0 0 H692 V333 H370 Q350 333 340 325 L0 299 Z" fill="var(--photo-bg)"/>
    <path d="M8 299 H420 Q432 320 412 325 H30 Q8 325 8 305 Z" fill="var(--card-shadow)"/>
    <path d="M0 0 H312 L430 290 L340 325 Q340 290 320 240 Z" fill="#dcdcdc" opacity="0.6"/>
    <path d="M0 15 H290 Q302 15 307 25 L432 285 Q436 299 420 299 H42 Q30 299 28 287 L0 60 Z" fill="var(--card)" stroke="#ffffff" stroke-width="2"/>
  </svg>
  <div class="hero-photo" role="img" aria-label="Photo of a confident young professional in a white collared shirt holding a smartphone"></div>

  <div class="headline headline--skill">SKILL UP</div>
  <div class="headline headline--salary">SALARY UP</div>
  <div class="t subhead">UPCOMING KVL COURSES</div>
  <div class="t tagline" style="top:243px">MEN &amp; WOMEN &nbsp;&nbsp;| &nbsp;&nbsp;IN-PERSON &amp; REMOTE &nbsp;&nbsp;|</div>
  <div class="t tagline" style="top:265px">PARTIAL SCHOLORASHIPS</div>

  <!-- Harbor Lantern Course -->
  <div class="section-tab" style="left:0;top:368px;width:222px"><span class="section-title" style="left:28px">HARBOR LANTERN</span></div>
  <div class="t label" style="left:28px;top:429px">BUSINESS SKILLS &amp; KNOWLEDGE TO</div>
  <svg class="tick" style="left:29px;top:454px"><use href="#tick"/></svg><div class="t item" style="left:53px;top:454px">Impress your interviewer</div>
  <svg class="tick" style="left:29px;top:477px"><use href="#tick"/></svg><div class="t item" style="left:53px;top:477px">Maximize Income</div>
  <svg class="tick" style="left:29px;top:499px"><use href="#tick"/></svg><div class="t item" style="left:53px;top:499px">Start / Run Your Business</div>
  <div class="badge badge--teal" style="left:237px;top:463px">4-5<br>MONTHS<br>NOV 2025</div>
  <div class="t label" style="left:28px;top:529px">PARTIAL LISTING</div>
  <svg class="tick" style="left:29px;top:554px"><use href="#tick"/></svg><div class="t item" style="left:53px;top:554px">Computers</div>
  <svg class="tick" style="left:29px;top:577px"><use href="#tick"/></svg><div class="t item" style="left:53px;top:577px">Marketing</div>
  <svg class="tick" style="left:29px;top:599px"><use href="#tick"/></svg><div class="t item" style="left:53px;top:599px">Sales</div>
  <svg class="tick" style="left:29px;top:622px"><use href="#tick"/></svg><div class="t item" style="left:53px;top:622px">Finance</div>
  <svg class="tick" style="left:29px;top:648px"><use href="#tick"/></svg><div class="t item" style="left:52px;top:648px">Investments</div>
  <svg class="tick" style="left:29px;top:670px"><use href="#tick"/></svg><div class="t item" style="left:52px;top:670px">Real Estate</div>
  <svg class="tick" style="left:139px;top:554px"><use href="#tick"/></svg><div class="t item" style="left:163px;top:554px">LedgerBooks</div>
  <svg class="tick" style="left:139px;top:577px"><use href="#tick"/></svg><div class="t item" style="left:163px;top:577px">Healthcare</div>
  <svg class="tick" style="left:139px;top:599px"><use href="#tick"/></svg><div class="t item" style="left:163px;top:599px">Business Strategy</div>
  <svg class="tick" style="left:139px;top:624px"><use href="#tick"/></svg><div class="t item" style="left:163px;top:624px">Communication</div>
  <svg class="tick" style="left:139px;top:648px"><use href="#tick"/></svg><div class="t item" style="left:163px;top:648px">Accounting</div>

  <!-- Bookkeeping -->
  <div class="section-tab" style="left:0;top:718px;width:268px"><span class="section-title" style="left:28px">BOOKKEEPING LEDGERBOOKS</span></div>
  <div class="t note" style="left:28px;top:776px">Train for a quality job</div>
  <div class="t note" style="left:28px;top:792px">Manage your own books</div>
  <svg class="tick" style="left:30px;top:817px"><use href="#tick"/></svg><div class="t item" style="left:54px;top:817px">Finance Management</div>
  <svg class="tick" style="left:30px;top:840px"><use href="#tick"/></svg><div class="t item" style="left:54px;top:840px">Customer &amp; Vendor Mgmt.</div>
  <svg class="tick" style="left:30px;top:862px"><use href="#tick"/></svg><div class="t item" style="left:54px;top:862px">Advanced Tools</div>
  <div class="badge badge--navy" style="left:228px;top:780px">5<br>WEEKS<br>NOV 2025</div>

  <!-- Software -->
  <div class="section-tab section-tab--right" style="left:377px;top:347px;width:315px"><span class="section-title" style="left:24px">SOFTWARE, WEB &amp; APPS</span></div>
  <div class="t note" style="left:404px;top:397px">#2 Best Tech Job</div>
  <div class="t note" style="left:401px;top:412px">National Career Review 2025</div>
  <div class="t label" style="left:401px;top:437px">JOB OPPORTUNITIES</div>
  <svg class="tick" style="left:403px;top:462px"><use href="#tick"/></svg><div class="t item" style="left:427px;top:462px">Computer Programmer</div>
  <svg class="tick" style="left:403px;top:485px"><use href="#tick"/></svg><div class="t item" style="left:427px;top:485px">Software Developer/Mobile</div>
  <svg class="tick" style="left:403px;top:507px"><use href="#tick"/></svg><div class="t item" style="left:427px;top:507px">Engineer Developer (Apps)</div>
  <div class="badge badge--teal" style="left:602px;top:405px">NOV<br>2025</div>
  <div class="t label" style="left:401px;top:537px">OPTIONAL</div>
  <div class="t item" style="left:403px;top:561px">Bachelors in Prog. &amp;Tech.</div>

  <!-- IT Support -->
  <div class="section-tab section-tab--right" style="left:376px;top:594px;width:316px"><span class="section-title section-title--long" style="left:24px">IT DESKTOP &amp; NETWORKING SUPPORT</span></div>
  <div class="t note" style="left:401px;top:644px">#2 Best Job</div>
  <div class="t note" style="left:401px;top:659px">National Career Review 2025</div>
  <div class="t label" style="left:403px;top:684px">JOB OPPORTUNITIES</div>
  <svg class="tick" style="left:403px;top:710px"><use href="#tick"/></svg><div class="t item" style="left:427px;top:710px">Desktop OS</div>
  <svg class="tick" style="left:403px;top:732px"><use href="#tick"/></svg><div class="t item" style="left:427px;top:732px">Networks</div>
  <svg class="tick" style="left:513px;top:710px"><use href="#tick"/></svg><div class="t item" style="left:537px;top:710px">Servers</div>
  <svg class="tick" style="left:513px;top:732px"><use href="#tick"/></svg><div class="t item" style="left:537px;top:732px">Cloud</div>
  <div class="badge badge--navy" style="left:600px;top:653px">7<br>MONTHS<br>Dec 2025</div>

  <!-- Office -->
  <div class="section-tab section-tab--right" style="left:376px;top:761px;width:316px"><span class="section-title" style="left:24px">DESKTOP OFFICE- COMPUTERS</span></div>
  <div class="t label" style="left:403px;top:817px">THE NEW JOB PREREQUISITE</div>
  <svg class="tick" style="left:403px;top:843px"><use href="#tick"/></svg><div class="t item" style="left:427px;top:843px">Sheets</div>
  <svg class="tick" style="left:403px;top:865px"><use href="#tick"/></svg><div class="t item" style="left:427px;top:865px">Email</div>
  <svg class="tick" style="left:495px;top:843px"><use href="#tick"/></svg><div class="t item" style="left:519px;top:843px">Documents</div>
  <svg class="tick" style="left:495px;top:865px"><use href="#tick"/></svg><div class="t item" style="left:519px;top:865px">Slides</div>
  <div class="badge badge--navy" style="left:602px;top:810px">5<br>WEEKS<br>DEC 2025</div>
  <div class="t item mint" style="left:403px;top:891px">Computer lab available to practice</div>
</main>
</body>
</html>
```